Design Creative Banner or Gif Ads. 3 Designs To Be Selected

Come up with some creative banner ads for stonewell.co.nz

*At least 3 different winning banners will be chosen*

Please provide banner ads / gif ads in common google ads / website banner formats.

They can be gif or static but must stand out while still maintaining clear clean text and visuals, with a premium professional feel (please avoid clip art or anything that gives a cheap message).

Please keep in mind that these will likely be small ads so text needs to be large and if there's there a lot of text then use multiple frames/ pages as submit as a gif.

Style
Minimal & clean lines
Architectural or realistic images
Avoid cartoon styles, clipart, or anything that looks cheap

Font
Nexa or Montserrat or similar

Tone
Premium, serious, trustworthy — fits new builds

Colours
Option 1: Deep Navy (trust & quality) & lighter blues and warm grey
Option 2: Open to bright colours to help the ads stand out, such as (but not limited to) bright pink with black, yellow, fluorescent green, provided the messaging is still done professionally.
Our logo is attached (Stone Well Logo)

Display Sizes
Ad specs for file sizes should be file formats like JPEG, GIF, and PNG, with animations limited to a max of 30 seconds or less.
We will need several different ad sizes provided for each of the 3 selected winning designs.

• Medium Rectangle: 300 × 250 pixels
• Leaderboard: 728 × 90 pixels
• Desktop Banner ad image: (640x360 pixels)
• Desktop Banner ad image 2: (300x600 pixels)
• Possibly one or two other sizes

Flexibility to be creative
The ad text, words, upper/lower case, layout, colour, theme, and images can be adjusted to how you think it will look best. The follow example ads are just examples of what we are after but we are keen to see what you can create.

Recommendations at this point:
1. Avoid text heavy
2. Looking for more Gif ads
3. Imaging: if possible use real stock photo's rather than AI

Themes:

1
Building Soon? Start Here
Free Build Planning Pack:
✓ Build Cost Calculator
✓ Hidden Cost Checklist
✓ Builder Comparison Guide
Build With Confidence
Download Free

2
Before You Choose A Builder
Compare Price, Scope, Risk & Value
Avoid Costly Mistakes
Choose The Right Builder With Confidence
Download The Free Guide

3
Planning A New Build?
Avoid These Common Mistakes:
✗ Hidden Exclusions
✗ Missing Scope
✗ Unrealistic Allowances
✗ Budget Blowouts
Download The Free Guide

4
Before You Buy Land
Know what it could cost to build.
Avoid Costly Building Mistakes
Download Our Free Guides

5
Know Your Build Budget?
• Free Build Cost Calculator
• Hidden Cost Checklist
• Build Planning Tools
Calculate Costs (Download)

Target Market(s)

Landowners looking to build

Industry/Entity Type

Building

Font styles to use
Other font styles liked:
• Nexa or Montserrat or similar

Requirements
Should not have
• Avoid cartoon styles, clipart, or anything that looks cheap

```html
<!DOCTYPE html>
<html lang="en">
<head>
<meta charset="utf-8">
<title>Stone Well Banner Set</title>
<link href="https://fonts.googleapis.com/css2?family=Montserrat:wght@400;500;600;700&display=swap" rel="stylesheet">
<style>
  :root{
    --stage:#4d4d4d;
    --navy:#1f2a3b;
    --navy-deep:#15202f;
    --sky:#3aa3d8;
    --stripe:#2a7fd0;
    --white:#ffffff;
    --ink:#1c2636;
    --photo-a:#5b6068;
    --photo-b:#2b2f36;
  }
  *{margin:0;padding:0;box-sizing:border-box}
  html,body{width:1200px;height:1001px;overflow:hidden;background:var(--stage);font-family:"Montserrat",sans-serif}
  .banner{position:absolute;overflow:hidden}
  .banner > svg.backdrop{position:absolute;left:0;top:0}
  .t{position:absolute;white-space:nowrap;line-height:1.1}
  .brand{position:absolute;display:flex;align-items:center;gap:8px;color:var(--ink);font-weight:600;white-space:nowrap}
  .brand-square{background:var(--ink);display:block}
  .btn{position:absolute;background:var(--sky);color:var(--white);border-radius:2px;display:flex;align-items:center}

  /* Medium rectangle */
  .rect-ad{left:58px;top:239px;width:421px;height:351px}
  .rect-ad .h-white{color:var(--white);font-weight:700;font-size:27px;left:30px;top:37px}
  .rect-ad .h-blue{color:var(--sky);font-weight:600;font-size:27px;left:30px}
  .rect-ad .sub{color:var(--white);font-weight:500;font-size:14.5px;left:30px;top:130px}
  .rect-ad .rule{position:absolute;left:30px;top:158px;width:190px;height:1px;background:var(--sky)}
  .rect-ad .pack{color:var(--white);font-weight:500;font-size:15px;left:30px;top:170px}
  .checks{position:absolute;left:30px;top:196px;list-style:none;color:var(--white);font-size:12px}
  .checks li{display:flex;align-items:center;gap:6px;height:20px}
  .rect-ad .btn{left:26px;top:270px;width:172px;height:33px;padding-left:14px;gap:9px}
  .btn-label{display:flex;flex-direction:column;line-height:1}
  .btn-label b{font-size:13px;font-weight:700;letter-spacing:.5px}
  .btn-label small{font-size:6px;font-weight:500;letter-spacing:.4px;margin-top:3px}
  .rect-ad .tag{color:var(--ink);font-weight:500;font-size:12.5px;right:30px;text-align:right;line-height:1.3;top:259px}
  .rect-ad .brand{left:226px;top:303px;font-size:21px}
  .rect-ad .brand-square{width:22px;height:22px}

  /* Desktop banner */
  .wide-ad{left:508px;top:239px;width:622px;height:351px}
  .wide-ad .h-white{color:var(--white);font-weight:700;font-size:22px;left:60px;top:42px}
  .wide-ad .h-blue{color:var(--sky);font-weight:600;font-size:19.5px;left:60px}
  .wide-ad .rule{position:absolute;left:60px;top:134px;width:264px;height:1px;background:var(--sky)}
  .wide-ad .body{color:var(--white);font-size:11.5px;font-weight:500;left:60px;top:145px;line-height:1.35}
  .wide-ad .kicker{color:var(--sky);font-size:10px;font-weight:600;letter-spacing:.3px;left:60px;top:189px}
  .wide-ad .btn{left:58px;top:213px;width:164px;height:25px;justify-content:center;gap:7px;font-size:11.5px;font-weight:700;letter-spacing:.8px}
  .wide-ad .tag{color:var(--ink);font-size:10.5px;font-weight:500;left:60px;top:277px}
  .wide-ad .brand{left:60px;top:298px;font-size:26px}
  .wide-ad .brand-square{width:28px;height:28px}

  /* Leaderboard */
  .strip-ad{left:59px;top:640px;width:1070px;height:132px}
  .strip-ad .brand{left:26px;top:42px;font-size:30px}
  .strip-ad .brand-square{width:32px;height:32px}
  .strip-ad .claim{color:var(--ink);font-size:13.5px;font-weight:500;left:26px;top:84px}
  .strip-ad .ask{color:var(--white);font-weight:600;font-size:24px;left:343px;top:46px;line-height:1.12}
  .strip-ad .calc-big{color:var(--sky);font-weight:700;font-size:32px;left:541px;top:42px;letter-spacing:.5px}
  .strip-ad .calc-small{color:var(--white);font-weight:600;font-size:17.5px;left:542px;top:78px;letter-spacing:2px}
  .strip-ad .btn{left:766px;top:34px;width:263px;height:66px;padding-left:22px;gap:12px;border-radius:3px}
  .strip-ad .btn-label b{font-size:26px;letter-spacing:0}
  .strip-ad .btn-label small{font-size:12.5px;letter-spacing:2.2px;margin-top:2px}
</style>
</head>
<body>

<!-- Medium rectangle -->
<section class="banner rect-ad">
  <svg class="backdrop" width="421" height="351" viewBox="0 0 421 351">
    <defs>
      <linearGradient id="photoA" x1="0" y1="0" x2="1" y2="1">
        <stop offset="0" stop-color="var(--photo-a)"/>
        <stop offset="1" stop-color="var(--photo-b)"/>
      </linearGradient>
    </defs>
    <rect width="421" height="351" fill="var(--navy)"/>
    <g role="img" aria-label="Smiling man in a dark suit with arms crossed in front of a modern apartment building">
      <polygon points="236,0 421,0 421,217 222,257 222,60" fill="url(#photoA)"/>
    </g>
    <polygon points="0,290 421,213 421,217 0,301" fill="var(--stripe)"/>
    <polygon points="0,301 421,217 421,351 0,351" fill="var(--white)"/>
  </svg>
  <div class="t h-white">Bought Land?</div>
  <div class="t h-blue" style="top:68px">Avoid Costly</div>
  <div class="t h-blue" style="top:100px">Build Mistakes</div>
  <div class="t sub">Discover The Hidden Costs</div>
  <div class="rule"></div>
  <div class="t pack">Free Build Planning Pack</div>
  <ul class="checks">
    <li><svg width="14" height="14" viewBox="0 0 14 14"><circle cx="7" cy="7" r="7" fill="var(--sky)"/><path d="M4 7.2l2 2 4-4.2" stroke="#fff" stroke-width="1.6" fill="none"/></svg>Build Cost Calculator</li>
    <li><svg width="14" height="14" viewBox="0 0 14 14"><circle cx="7" cy="7" r="7" fill="var(--sky)"/><path d="M4 7.2l2 2 4-4.2" stroke="#fff" stroke-width="1.6" fill="none"/></svg>Build Journey Roadmap</li>
    <li><svg width="14" height="14" viewBox="0 0 14 14"><circle cx="7" cy="7" r="7" fill="var(--sky)"/><path d="M4 7.2l2 2 4-4.2" stroke="#fff" stroke-width="1.6" fill="none"/></svg>Hidden Cost Checklist</li>
  </ul>
  <div class="btn">
    <svg width="18" height="18" viewBox="0 0 18 18"><path d="M9 2v10M5 8l4 4 4-4M2 13v3h14v-3" stroke="#fff" stroke-width="1.3" fill="none"/></svg>
    <span class="btn-label"><b>DOWNLOAD</b><small>(FREE BUILD PLANNING PACK)</small></span>
  </div>
  <div class="t tag">Choose The Right Builder<br>With Clarity &amp; Confidence.</div>
  <div class="brand"><span class="brand-square"></span>Stone Well</div>
</section>

<!-- Desktop banner -->
<section class="banner wide-ad">
  <svg class="backdrop" width="622" height="351" viewBox="0 0 622 351">
    <defs>
      <linearGradient id="photoB" x1="0" y1="0" x2="1" y2="1">
        <stop offset="0" stop-color="var(--photo-a)"/>
        <stop offset="1" stop-color="var(--photo-b)"/>
      </linearGradient>
    </defs>
    <rect width="622" height="351" fill="var(--white)"/>
    <rect width="622" height="261" fill="var(--navy)"/>
    <rect y="261" width="340" height="4" fill="var(--stripe)"/>
    <g role="img" aria-label="Smiling man in a dark suit with arms crossed in front of a modern apartment building">
      <polygon points="420,0 622,0 622,351 344,351 324,230 370,100" fill="url(#photoB)"/>
    </g>
  </svg>
  <div class="t h-white">Bought Land?</div>
  <div class="t h-blue" style="top:80px">Before You Choose</div>
  <div class="t h-blue" style="top:107px">A Builder, Read This.</div>
  <div class="rule"></div>
  <div class="t body">Avoid Costly Mistakes, Budget Blowouts,<br>&amp; Contract Surprises.</div>
  <div class="t kicker">FREE BUILD PLANNING GUIDE</div>
  <div class="btn">
    <svg width="13" height="13" viewBox="0 0 18 18"><path d="M9 2v10M5 8l4 4 4-4M2 13v3h14v-3" stroke="#fff" stroke-width="1.5" fill="none"/></svg>
    DOWNLOAD NOW
  </div>
  <div class="t tag">Choose The Right Builder With Clarity &amp; Confidence.</div>
  <div class="brand"><span class="brand-square"></span>Stone Well</div>
</section>

<!-- Leaderboard -->
<section class="banner strip-ad">
  <svg class="backdrop" width="1070" height="132" viewBox="0 0 1070 132">
    <rect width="1070" height="132" fill="var(--navy)"/>
    <polygon points="0,0 347,0 295,132 0,132" fill="var(--white)"/>
    <path d="M510 36l12 32-12 32" stroke="var(--sky)" stroke-width="1.2" fill="none"/>
  </svg>
  <div class="brand"><span class="brand-square"></span>Stone Well</div>
  <div class="t claim">Compare Quotes From Trusted Builders</div>
  <div class="t ask">Planning<br>A New Build?</div>
  <div class="t calc-big">CALCULATE</div>
  <div class="t calc-small">YOUR BUILD COST</div>
  <div class="btn">
    <svg width="30" height="38" viewBox="0 0 30 38">
      <rect x="1" y="1" width="28" height="36" rx="3" stroke="#fff" stroke-width="2" fill="none"/>
      <rect x="5" y="5" width="20" height="7" stroke="#fff" stroke-width="1.6" fill="none"/>
      <g fill="#fff">
        <rect x="5" y="16" width="5" height="4"/><rect x="12.5" y="16" width="5" height="4"/><rect x="20" y="16" width="5" height="4"/>
        <rect x="5" y="23" width="5" height="4"/><rect x="12.5" y="23" width="5" height="4"/><rect x="20" y="23" width="5" height="4"/>
        <rect x="5" y="30" width="5" height="4"/><rect x="12.5" y="30" width="5" height="4"/><rect x="20" y="30" width="5" height="4"/>
      </g>
    </svg>
    <span class="btn-label"><b>FREE BUILD</b><small>COST CALCULATOR</small></span>
    <svg width="12" height="36" viewBox="0 0 12 36" style="margin-left:14px"><path d="M1 1l10 17L1 35" stroke="#fff" stroke-width="1.4" fill="none"/></svg>
  </div>
</section>

</body>
</html>
```